Clear Harbor Transportation Management Association

We are looking to design an awards certificate for an upcoming event that we are having in December. This award would be given to our employee members who have done an outstanding job of promoting commuting alternatives (biking, walking, transit, ridesharing) to driving alone, and as such have reduced green house gas emissions. We are looking for a cool graphic that will make the award something special and worth framing. Attached is our current logo which should be on the certificate somewhere, as well as a few of our program design logos which can be used for inspiration.

Target Market(s)

Board members

Industry/Entity Type

Event

Requirements
Must have
• Graphic suitable for framing as part of an awards certificate
Nice to have
• Something that relates to what we do which is promoting sustainable tranportation (biking, walking, transit, and ridesharing).

```html
<!DOCTYPE html>
<html lang="en">
<head>
<meta charset="utf-8">
<title>Certificate of Achievement – Clear Harbor TMA</title>
<link rel="stylesheet" href="https://fonts.googleapis.com/css2?family=Libre+Baskerville:ital@0;1&family=Carlito&display=swap">
<style>
  :root {
    --ink: #111111;
    --brand-blue: #1a8ac6;
    --paper: #ffffff;
    --trail-green: #7cbf5a;
    --trail-red: #ea6a4f;
    --trail-sky: #6fb9de;
    --trail-orange: #f2a53a;
    --trail-teal: #4fb2c4;
    --trail-olive: #a3b04a;
  }
  * { margin: 0; padding: 0; box-sizing: border-box; }
  html, body { width: 1200px; height: 927px; overflow: hidden; background: var(--paper); }
  .certificate {
    position: relative; width: 1200px; height: 927px; background: var(--paper);
    color: var(--ink);
    font-family: "Libre Baskerville", "Century Schoolbook", serif;
  }
  .frame-outer {
    position: absolute; left: 18px; top: 12px; width: 1158px; height: 901px;
    border: 5px solid var(--ink);
  }
  .frame-inner {
    position: absolute; left: 31px; top: 23px; width: 1132px; height: 878px;
    border: 1.5px solid var(--ink);
  }
  .brand {
    position: absolute; left: 0; top: 78px; width: 100%;
    display: flex; justify-content: center; align-items: center; gap: 12px;
  }
  .brand-dot { width: 22px; height: 22px; border-radius: 50%; background: var(--brand-blue); }
  .brand-name { font-size: 34px; font-weight: 400; color: var(--brand-blue); }
  .title {
    position: absolute; left: 0; top: 160px; width: 100%; text-align: center;
    font-style: italic; font-weight: 400; font-size: 64px; color: var(--brand-blue);
  }
  .line {
    position: absolute; left: 0; width: 100%; text-align: center;
    font-style: italic; font-size: 20px; line-height: 27px;
  }
  .awarded { top: 263px; }
  .recipient-line {
    position: absolute; left: 115px; top: 361px; width: 966px;
    border-top: 1.5px dotted var(--ink);
  }
  .citation { top: 400px; font-size: 19px; }
  .date { top: 486px; font-size: 21px; }
  .venue { top: 536px; font-size: 21px; }
  .sign {
    position: absolute; top: 673px;
    font-family: "Carlito", "Calibri", sans-serif; font-size: 21px;
  }
  .sign-accredited { left: 208px; }
  .sign-signature { left: 680px; }
  .trail { position: absolute; left: 0; top: 0; }
  .programs {
    position: absolute; top: 851px; left: 0; width: 100%;
    font-family: "Carlito", "Calibri", sans-serif; font-size: 15.5px;
  }
  .program { position: absolute; transform: translateX(-50%); white-space: nowrap; }
</style>
</head>
<body>
<main class="certificate">
  <div class="frame-outer"></div>
  <div class="frame-inner"></div>

  <header class="brand">
    <span class="brand-dot"></span>
    <span class="brand-name">Clear Harbor TMA</span>
  </header>

  <h1 class="title">Certificate of Achievement</h1>

  <p class="line awarded">This Certilficate is awarded to</p>
  <div class="recipient-line"></div>

  <p class="line citation">For doing outstanding job of promoting Community Alternatives (biking, walking, transit and ridesharing)<br>Thus reducing green house gas emmissions</p>

  <p class="line date">On this................................day of................December, 2015</p>
  <p class="line venue">At................................Given by.......................................</p>

  <p class="sign sign-accredited">Accredited by................................</p>
  <p class="sign sign-signature">Signature................................</p>

  <svg class="trail" width="1200" height="927" viewBox="0 0 1200 927">
    <rect x="62" y="745" width="162" height="86" rx="8" fill="var(--trail-green)" opacity="0.22" role="img" aria-label="Line illustration of a house and car for Guaranteed Ride Home"/>
    <rect x="234" y="772" width="178" height="58" rx="8" fill="var(--trail-red)" opacity="0.22" role="img" aria-label="Line illustration of a shared car between two houses for Ride Matching"/>
    <rect x="448" y="762" width="148" height="68" rx="8" fill="var(--trail-sky)" opacity="0.22" role="img" aria-label="Line illustration of an express bus and ferry for Express Yourself"/>
    <rect x="618" y="768" width="138" height="62" rx="8" fill="var(--trail-orange)" opacity="0.22" role="img" aria-label="Line illustration of a carpool car for Carpool Subsidy"/>
    <rect x="768" y="750" width="128" height="80" rx="8" fill="var(--trail-teal)" opacity="0.22" role="img" aria-label="Line illustration of walking and cycling for Workout to Work"/>
    <rect x="958" y="762" width="172" height="68" rx="8" fill="var(--trail-olive)" opacity="0.22" role="img" aria-label="Line illustration of a vanpool van for Vanpool Subsidy"/>
  </svg>

  <div class="programs">
    <span class="program" style="left:134px">Guaranteed Ride Home</span>
    <span class="program" style="left:316px">Ride Matching</span>
    <span class="program" style="left:503px">Express Yourself</span>
    <span class="program" style="left:680px">Carpool Subsidy</span>
    <span class="program" style="left:843px">Workout to Work</span>
    <span class="program" style="left:1023px">Vanpool Subsidy</span>
  </div>
</main>
</body>
</html>
```